Our new all natural drink needs a product design (logo and front-pack).
We developed an innovative alternative under the brand name "Plain Sip Co" - all natural and great tasting soft drink and ice tea, beyond the conventional big commercial brands. Our ambition is to set a new high standard for soft drinks and ice tea, produced in a simple honest manner.

Target Market(s)

European markets

Colors

Designer to choose colors to be used in the design.

Requirements
Must have
• We want “clean” minimalist design with focus on the number “1”, but also to present the ingredients we have inside the different flavor variants (see the brief attached)
• We also want to be visible and easy recognizable on the shelves in-store
Nice to have
• Product benefits: 100% natural products. No white sugar, aromas, colors, additives, artificial substances, citric acids or ascorbic acids allowed.
• We focus on the highest quality possible and superior natural taste experiences. In general, no compromises!
Should not have
• Must not be overcrowded and with too much colors. Must not have similarities with the conventional big commercial brands (e.g. Fizzmora, Bruvo, etc.)

```html
<!DOCTYPE html>
<html lang="en">
<head>
<meta charset="utf-8">
<title>Plain Sip Co – Lemon with Ironwort</title>
<link rel="stylesheet" href="https://fonts.googleapis.com/css2?family=Yellowtail&family=Kaushan+Script&family=PT+Sans+Narrow:wght@400;700&display=swap">
<style>
  :root {
    --bg: #ffffff;
    --bottle: #fdc300;
    --cap: #7a6e5e;
    --cap-light: #b0a89b;
    --neck: #c9c9c9;
    --green: #6ccb4a;
    --sun: #fdfc62;
    --blue: #4282fc;
    --blue-glow: #7de6f5;
    --red: #fe0000;
    --panel: #ffc864;
    --juice: #fde34a;
    --juice-light: #fff5a8;
    --ink: #111111;
    --accent-blue: #4a7ae6;
    --white: #ffffff;
  }
  html, body {
    margin: 0;
    padding: 0;
    width: 1200px;
    height: 1200px;
    overflow: hidden;
    background: var(--bg);
  }
  .canvas { display: block; width: 1200px; height: 1200px; }
  .brand-name { font-family: "PT Sans Narrow", sans-serif; font-weight: 700; fill: var(--ink); }
  .flavour { font-family: "Yellowtail", cursive; fill: var(--ink); font-size: 27px; }
  .claim-figure { font-family: "Kaushan Script", cursive; fill: var(--accent-blue); font-size: 70px; }
  .claim-copy { font-family: "PT Sans Narrow", sans-serif; font-weight: 700; fill: var(--ink); font-size: 21px; letter-spacing: 1.3px; }
  .maker { font-family: "PT Sans Narrow", sans-serif; fill: var(--ink); font-size: 25px; }
</style>
</head>
<body>
<svg class="canvas" viewBox="0 0 1200 1200" xmlns="http://www.w3.org/2000/svg">
  <defs>
    <clipPath id="label-area"><rect x="399" y="353" width="732" height="634"/></clipPath>
    <clipPath id="label-top">
      <path d="M399,353 H1131 V590 C1000,530 840,540 760,600 C620,720 470,740 399,653 Z"/>
    </clipPath>
    <radialGradient id="blue-field" cx="800" cy="930" r="360" gradientUnits="userSpaceOnUse">
      <stop offset="0" stop-color="var(--blue-glow)"/>
      <stop offset="1" stop-color="var(--blue)"/>
    </radialGradient>
    <radialGradient id="juice-tone" cx="0.5" cy="0.5" r="0.6">
      <stop offset="0" stop-color="var(--juice-light)"/>
      <stop offset="1" stop-color="var(--juice)"/>
    </radialGradient>
  </defs>

  <!-- corner brand -->
  <g class="corner-brand">
    <circle cx="78" cy="110" r="26" fill="var(--ink)"/>
    <text class="brand-name" x="116" y="124" font-size="40">Plain Sip Co</text>
  </g>

  <!-- bottle -->
  <g class="bottle">
    <rect class="bottle-neck" x="496" y="178" width="181" height="28" fill="var(--neck)"/>
    <rect class="bottle-cap" x="467" y="83" width="237" height="97" fill="var(--cap)"/>
    <rect x="503" y="83" width="37" height="97" fill="var(--cap-light)"/>
    <rect x="665" y="83" width="14" height="97" fill="var(--cap-light)"/>
    <path class="bottle-body" fill="var(--bottle)"
      d="M506,200 H662 A107,107 0 0 1 769,307 V1092 A32,32 0 0 1 737,1124 H431 A32,32 0 0 1 399,1092 V307 A107,107 0 0 1 506,200 Z"/>
  </g>

  <!-- front label -->
  <g class="label" clip-path="url(#label-area)">
    <rect class="label-lower" x="399" y="353" width="732" height="634" fill="url(#blue-field)"/>
    <circle class="label-red-disc" cx="627" cy="640" r="172" fill="var(--red)"/>
    <g class="label-upper" clip-path="url(#label-top)">
      <rect x="399" y="353" width="732" height="400" fill="var(--green)"/>
      <circle class="label-sun" cx="613" cy="400" r="148" fill="var(--sun)"/>
    </g>
    <path class="label-wave" fill="none" stroke="var(--white)" stroke-width="6"
      d="M399,653 C470,740 620,720 760,600 C840,540 1000,530 1131,590"/>

    <rect class="juice-splash" role="img" aria-label="Illustration of a lemon juice splash"
      x="440" y="668" width="425" height="240" rx="24" fill="url(#juice-tone)"/>

    <text class="brand-name" x="470" y="560" font-size="76">Plain Sip</text>
    <text class="brand-name" x="560" y="640" font-size="76">Co</text>

    <path class="claim-panel" fill="var(--panel)"
      d="M873,573 C960,545 1060,550 1131,590 V933 H873 Z"/>
    <rect class="maker-band" x="873" y="933" width="258" height="54" fill="var(--red)"/>
  </g>

  <!-- flavour badge -->
  <g class="flavour-badge">
    <circle cx="870" cy="473" r="104" fill="var(--red)"/>
    <circle cx="870" cy="473" r="82" fill="var(--sun)"/>
    <text class="flavour" text-anchor="middle">
      <tspan x="870" y="442">Lemon</tspan>
      <tspan x="870" y="482">with</tspan>
      <tspan x="870" y="522">Ironwort</tspan>
    </text>
  </g>

  <!-- claim -->
  <g class="claim">
    <text class="claim-figure" x="1005" y="705" text-anchor="middle">100%</text>
    <text class="claim-copy">
      <tspan x="893" y="763">NATURAL product</tspan>
      <tspan x="893" y="785">with local ingredients</tspan>
      <tspan x="893" y="807">that will give you an</tspan>
      <tspan x="893" y="829">invigorating taste</tspan>
      <tspan x="893" y="851">experience and will</tspan>
      <tspan x="893" y="873">keep you refreshed</tspan>
      <tspan x="893" y="895">throughout the day</tspan>
    </text>
    <text class="maker" x="1002" y="969" text-anchor="middle">Norvane Company</text>
  </g>
</svg>
</body>
</html>
```